EPS Recycling End Market Infographic

We need a two-page visual presentation of new end-market applications for recycled expanded polystyrene (EPS) collected for recycling. This focuses on expanded polystyrene (foam) transport packaging used for international distribution of goods, including pharmaceuticals and food, electronics, appliances and other products that need superior packaging protection.

The bulletin will have examples of 5 major industry categories that benefit from recycled EPS feedstock for reverse engineering to meet current market demand. It will also showcase names of companies that use recycled content EPS in their product manufacturing to legitimize end market adoption. The capability to use recycled EPS in new EPS packaging should be highlighted. We would like this bulletin to demonstrate the widespread application of recycled EPS in different industries and establish credibility that it is being used in a variety of interesting recycled-content products. We welcome creative and interesting font treatments and new trends in graphic design.

Target Market(s)

International Government Agencies, Packaging Engineers, Big Box Retailers, & Environmental Professionals

Industry/Entity Type

Plastic Manufacturers

Font styles to use
Sans Serif

Requirements
Must have
• Visual focus points, multiple examples of products and manufacturers as evidence to the information content
Should not have
• Insufficient white space or outdated design elements (like two-tone gradients).

```html
<!DOCTYPE html>
<html lang="en">
<head>
<meta charset="utf-8">
<title>Recycled EPS and Markets</title>
<link rel="stylesheet" href="https://fonts.googleapis.com/css2?family=Montserrat:wght@400;500;600;700;800;900&family=Poppins:wght@400;500;600;700&display=swap">
<style>
:root{
  --backdrop:#5d7f98;
  --paper:#ffffff;
  --gold:#b79b48;
  --gold-dark:#9a8035;
  --olive:#8f9c3e;
  --orange:#e8922c;
  --ink:#2b2b2b;
  --muted:#5a5a5a;
  --light:#f1efe6;
}
*{margin:0;padding:0;box-sizing:border-box}
html,body{width:1200px;height:2724px;overflow:hidden}
body{background:var(--backdrop);font-family:"Poppins",sans-serif;color:var(--ink);position:relative}
.page{position:absolute;left:112px;width:976px;background:var(--paper);overflow:hidden;box-shadow:0 6px 24px rgba(0,0,0,.25)}
.page-one{top:80px;height:1160px}
.page-two{top:1290px;height:1340px}
.abs{position:absolute}

/* page one */
.hero-band{left:0;top:0;width:976px;height:250px;background:var(--gold)}
.hero-title{left:56px;top:44px;color:#fff;font-family:"Montserrat",sans-serif;font-weight:900;line-height:.95}
.hero-title .big{font-size:100px;letter-spacing:1px;display:block}
.hero-title .small{font-size:54px;display:block;margin-top:10px}
.brand{display:flex;align-items:center;gap:12px;font-family:"Poppins",sans-serif;font-weight:600}
.brand .mark{width:30px;height:30px;background:currentColor;flex:none}
.hero-brand{right:44px;top:70px;color:#fff;font-size:22px;width:210px;line-height:1.15}
.hero-brand .mark{width:40px;height:40px}
.cooler-photo{left:560px;top:190px;width:380px;height:380px;border-radius:50%;border:10px solid #fff;background:radial-gradient(circle at 45% 40%,#fafafa 0%,#dfe3e6 55%,#a8b3bb 100%);box-shadow:0 4px 14px rgba(0,0,0,.15)}
.cooler-tag{left:600px;top:480px;background:#fff;padding:10px 20px;border-radius:6px;box-shadow:0 2px 8px rgba(0,0,0,.15);font-family:"Montserrat",sans-serif}
.cooler-tag small{display:block;font-size:14px;color:var(--muted);font-weight:500}
.cooler-tag strong{font-size:28px;color:var(--gold-dark);font-weight:800}
.recycle-icon{left:58px;top:286px}
.stat{left:56px;top:390px;font-family:"Montserrat",sans-serif;color:var(--gold)}
.stat .num{font-size:84px;font-weight:900;line-height:1}
.stat .unit{font-size:34px;font-weight:800;margin-left:8px}
.stat .desc{font-size:30px;font-weight:800;line-height:1.15;color:var(--gold-dark);margin-top:8px;width:440px}
.intro{left:56px;top:640px;width:864px;font-size:21px;line-height:1.5;color:var(--ink)}
.category-panel{left:40px;top:770px;width:896px;height:270px;background:var(--olive);border-radius:6px}
.panel-num{left:26px;top:20px;font-family:"Montserrat",sans-serif;font-weight:900;font-size:200px;color:#fff;line-height:1}
.panel-caption{left:200px;top:78px;width:150px;font-size:16px;font-weight:600;color:#fff;line-height:1.3}
.category-list{left:370px;top:30px;width:505px;display:grid;grid-template-columns:1fr 1fr;gap:22px 18px}
.category{display:flex;align-items:center;gap:12px;color:#fff;font-family:"Montserrat",sans-serif;font-weight:700;font-size:19px;line-height:1.15}
.category .icon{width:52px;height:52px;border-radius:50%;background:#fff;flex:none;display:flex;align-items:center;justify-content:center}
.footer{left:40px;bottom:36px;width:896px;display:flex;align-items:center;justify-content:space-between;gap:24px;font-size:14px;color:var(--muted)}
.footer span{white-space:nowrap}
.footer .brand{color:var(--gold-dark);font-size:16px;white-space:nowrap}

/* page two */
.headline{left:60px;top:56px;width:450px;font-family:"Montserrat",sans-serif;color:var(--ink)}
.headline .lead{font-size:40px;font-weight:500}
.headline .main{font-size:40px;font-weight:800;line-height:1.15}
.headline .accent{font-size:86px;font-weight:800;color:var(--olive);line-height:1.05;display:block;margin-top:6px}
.headline-bar{left:0;top:345px;width:44px;height:10px;background:var(--olive)}
.auto-photo{left:530px;top:48px;width:400px;height:230px;border-radius:10px;background:linear-gradient(160deg,#4a4a4a,#1e1e1e)}
.badge{width:52px;height:52px;border-radius:50%;background:var(--olive);color:#fff;font-family:"Montserrat",sans-serif;font-weight:800;font-size:22px;display:flex;align-items:center;justify-content:center;border:4px solid #fff}
.auto-badge{left:560px;top:252px}
.auto-label{left:630px;top:292px;font-family:"Montserrat",sans-serif}
.auto-label strong{display:block;font-size:28px;font-weight:800;line-height:1.15}
.auto-label span{font-size:18px;color:var(--muted)}
.product-row{left:40px;top:430px;width:896px;display:grid;grid-template-columns:repeat(5,1fr);gap:18px}
.product{position:relative;text-align:center;font-family:"Montserrat",sans-serif}
.product .photo{height:170px;border-radius:8px;background:linear-gradient(180deg,#eef1f3,#c9d2d8)}
.product .badge{position:absolute;top:146px;left:50%;transform:translateX(-50%);width:48px;height:48px;font-size:20px}
.product strong{display:block;margin-top:38px;font-size:20px;font-weight:800;line-height:1.15}
.product span{font-size:14px;color:var(--muted)}
.more-section{left:40px;top:730px;width:896px;height:330px;background:var(--light);border-radius:10px}
.site-photo{left:0;top:0;width:470px;height:330px;border-radius:10px;background:linear-gradient(150deg,#b9b2a4,#7f7a70)}
.more-tag{left:170px;top:110px;width:280px;background:#fff;border-radius:8px;padding:18px 18px 18px 36px;box-shadow:0 3px 10px rgba(0,0,0,.15);font-family:"Montserrat",sans-serif}
.more-tag .badge{position:absolute;left:-26px;top:16px;background:var(--orange)}
.more-tag strong{display:block;font-size:25px;color:var(--orange);font-weight:800}
.more-tag span{font-size:14px;line-height:1.35;color:var(--ink)}
.more-list{left:500px;top:30px;width:370px;display:grid;grid-template-columns:1fr 1fr;gap:30px 20px}
.more-item{font-size:15px;line-height:1.3;color:var(--ink)}
.more-item .badge{width:46px;height:46px;font-size:19px;background:var(--orange);margin-bottom:10px;border-color:var(--light)}
.makers-band{left:40px;top:1100px;width:896px;height:140px;background:var(--olive);border-radius:6px}
.makers-title{left:24px;top:26px;width:180px;color:#fff;font-family:"Montserrat",sans-serif;font-weight:800;font-size:19px;line-height:1.25}
.makers-grid{left:215px;top:18px;width:665px;display:grid;grid-template-columns:repeat(5,1fr);gap:10px}
.maker{background:#fff;height:46px;border-radius:4px;display:flex;align-items:center;justify-content:center;font-size:14px;font-weight:600;color:var(--ink);text-align:center;line-height:1.1}
</style>
</head>
<body>

<section class="page page-one">
  <div class="abs hero-band"></div>
  <h1 class="abs hero-title"><span class="big">RECYCLED</span><span class="small">EPS AND MARKETS</span></h1>
  <div class="abs brand hero-brand"><span class="mark"></span>Polyfoam Trade Council</div>

  <div class="abs cooler-photo" role="img" aria-label="Photo of a white recycled-content EPS foam cooler"></div>
  <div class="abs cooler-tag"><small>Recycled Content</small><strong>EPS COOLER</strong></div>

  <svg class="abs recycle-icon" width="90" height="90" viewBox="0 0 24 24" fill="none" stroke="#b79b48" stroke-width="2" stroke-linecap="round" stroke-linejoin="round" aria-hidden="true">
    <path d="M7 19H4.8a1.8 1.8 0 0 1-1.6-2.7L5.5 12"/><path d="M11 19h8.2a1.8 1.8 0 0 0 1.6-2.7l-1.2-2"/><path d="M14 16l-3 3 3 3"/>
    <path d="M8.3 13.6L9 9.5 5 8.8"/><path d="M9 9.5l-1-1.7M9.3 5.4l.9-1.5a1.8 1.8 0 0 1 3 0l3.9 6.6"/><path d="M13.4 9.4l4 1.1 1-4"/>
  </svg>

  <div class="abs stat">
    <div><span class="num">30,800</span><span class="unit">TONS</span></div>
    <div class="desc">OF EXPANDED POLYSTYRENE (EPS) WAS RECYCLED IN 2022</div>
  </div>

  <p class="abs intro">Recycled Eps Foam Can Be Repurposed Into A Diverse Array Of Products Across Various Industries. These Applications Underscore The Versatility Of Recycled Eps, Contributing To Sustainability Across Multiple Sectors.</p>

  <div class="abs category-panel">
    <div class="abs panel-num">5.</div>
    <div class="abs panel-caption">Examples of Industry Categories That Benefit From EPS Recycled Content</div>
    <div class="abs category-list">
      <div class="category"><span class="icon"><svg width="28" height="28" viewBox="0 0 24 24" fill="none" stroke="#8f9c3e" stroke-width="2"><path d="M3 21h18M5 21V9l7-5 7 5v12M9 21v-6h6v6"/></svg></span>Construction &amp; Architectural</div>
      <div class="category"><span class="icon"><svg width="28" height="28" viewBox="0 0 24 24" fill="none" stroke="#8f9c3e" stroke-width="2"><path d="M6 3h12l-2 18H8z"/><path d="M7 9h10"/></svg></span>Textile &amp; Fiber</div>
      <div class="category"><span class="icon"><svg width="28" height="28" viewBox="0 0 24 24" fill="none" stroke="#8f9c3e" stroke-width="2"><rect x="3" y="5" width="18" height="14" rx="1"/><path d="M3 12h18M12 5v14"/></svg></span>Wood Composites &amp; Blends</div>
      <div class="category"><span class="icon"><svg width="28" height="28" viewBox="0 0 24 24" fill="none" stroke="#8f9c3e" stroke-width="2"><rect x="4" y="3" width="14" height="7" rx="1"/><path d="M18 6h2v6h-8v3M11 15h2v6h-2z"/></svg></span>Paints, Coatings, Adhesives</div>
      <div class="category"><span class="icon"><svg width="28" height="28" viewBox="0 0 24 24" fill="none" stroke="#8f9c3e" stroke-width="2"><path d="M9 3h6M10 3v6l-5 10a1.5 1.5 0 0 0 1.3 2h11.4a1.5 1.5 0 0 0 1.3-2l-5-10V3"/></svg></span>Additives</div>
    </div>
  </div>

  <div class="abs footer">
    <div class="brand"><span class="mark"></span>Polyfoam Trade Council</div>
    <span>460 Harbor Line Rd. Suite 12 Elmswood, MD 20990</span>
    <span>800-555-0142</span>
    <span>www.polyfoamcouncil.org</span>
  </div>
</section>

<section class="page page-two">
  <h2 class="abs headline">
    <span class="lead">Different</span><br>
    <span class="main">Products and Name of Manufacturer That Use EPS Recycled Content</span>
    <span class="accent">Examples</span>
  </h2>
  <div class="abs headline-bar"></div>

  <div class="abs auto-photo" role="img" aria-label="Photo of a black molded automotive foam component"></div>
  <div class="abs badge auto-badge">1.</div>
  <div class="abs auto-label"><strong>Automotive Components</strong><span>By Kestrel Forms</span></div>

  <div class="abs product-row">
    <div class="product"><div class="photo" role="img" aria-label="Photo of surfboard blanks"></div><div class="badge">2.</div><strong>Surfboard Blanks</strong><span>By Maren Boards</span></div>
    <div class="product"><div class="photo" role="img" aria-label="Photo of a blue patio bench"></div><div class="badge">3.</div><strong>Patio Bench</strong><span>By Ayla Outdoor</span></div>
    <div class="product"><div class="photo" role="img" aria-label="Photo of clothing hangers"></div><div class="badge">4.</div><strong>Clothing Hangers</strong><span>By Hangwell</span></div>
    <div class="product"><div class="photo" role="img" aria-label="Photo of a serving spoon"></div><div class="badge">5.</div><strong>Spoon</strong><span>By Ladle &amp; Co</span></div>
    <div class="product"><div class="photo" role="img" aria-label="Photo of picture frames"></div><div class="badge">6.</div><strong>Picture Frames</strong><span>By Framewell</span></div>
  </div>

  <div class="abs more-section">
    <div class="abs site-photo" role="img" aria-label="Photo of a building site with lightweight concrete insulation panels"></div>
    <div class="abs more-tag">
      <div class="badge">1.</div>
      <strong>More Examples</strong>
      <span>Lightweight Concrete Insulation Panels/Rooftop Gardens &amp; Soil Improvement</span>
    </div>
    <div class="abs more-list">
      <div class="more-item"><div class="badge">2.</div>3D Printing Filaments Used for Molding, Injection Molding &amp; Extrusion</div>
      <div class="more-item"><div class="badge">3.</div>Composite Binders Glue</div>
      <div class="more-item"><div class="badge">4.</div>Non-Woven Fabrics Fiber Absorbents Fillers</div>
      <div class="more-item"><div class="badge">5.</div>Protective &amp; Hydrophobic Coatings Adhesives &amp; Sealants</div>
    </div>
  </div>

  <div class="abs makers-band">
    <div class="abs makers-title">Global Manufacturers Vested In EPS Recycling</div>
    <div class="abs makers-grid">
      <div class="maker">Norvale</div>
      <div class="maker">Brightline</div>
      <div class="maker">Orbital Audio</div>
      <div class="maker">Eddyworks</div>
      <div class="maker">Skyhaven</div>
      <div class="maker">Valumart</div>
      <div class="maker">Koyama Motors</div>
      <div class="maker">Lumeva</div>
      <div class="maker">Helix Print</div>
      <div class="maker">Sunmark</div>
    </div>
  </div>

  <div class="abs footer">
    <div class="brand"><span class="mark"></span>Polyfoam Trade Council</div>
    <span>460 Harbor Line Rd. Suite 12 Elmswood, MD 20990</span>
    <span>800-555-0142</span>
    <span>www.polyfoamcouncil.org</span>
  </div>
</section>

</body>
</html>
```